Shadows over Briarwick Hall

We are hosting an open-to-the-public murder mystery dinner and masquerade ball on Oct. 31. I need a postcard design that we can display, hand out and mail for marketing.

We produce events in the KC area.

I'd like to see designs with a Halloween masquerade ball/murder mystery theme.

```html
<!DOCTYPE html>
<html lang="en">
<head>
<meta charset="utf-8">
<title>Shadows over Briarwick Hall — Postcard</title>
<link rel="stylesheet" href="https://fonts.googleapis.com/css2?family=Parisienne&family=Cabin:wght@400&display=swap">
<style>
  :root {
    --paper: #ffffff;
    --ink: #111111;
    --divider: #c9c9c9;
  }
  html, body {
    margin: 0;
    padding: 0;
    width: 1200px;
    height: 930px;
    overflow: hidden;
    background: var(--paper);
  }
  .postcard {
    position: relative;
    width: 1200px;
    height: 930px;
    background: var(--paper);
    color: var(--ink);
  }
  .invitation {
    position: absolute;
    left: 20px;
    top: 0;
    width: 540px;
    height: 800px;
    text-align: center;
  }
  .invitation > * {
    position: absolute;
    left: 0;
    width: 540px;
    margin: 0;
  }
  .lead-in {
    top: 45px;
    font-family: "Cabin", sans-serif;
    font-size: 34px;
    line-height: 44px;
  }
  .event-title {
    top: 102px;
    font-family: "Parisienne", cursive;
    font-weight: 400;
    font-size: 62px;
    line-height: 71px;
  }
  .tagline {
    top: 327px;
    font-family: "Cabin", sans-serif;
    font-size: 34px;
    line-height: 44px;
  }
  .details {
    top: 427px;
    font-family: "Parisienne", cursive;
    font-size: 48px;
    line-height: 66px;
  }
  .tickets {
    top: 637px;
    font-family: "Cabin", sans-serif;
    font-size: 32px;
    line-height: 49px;
  }
  .tickets a {
    color: var(--ink);
    text-decoration: underline;
  }
  .divider {
    position: absolute;
    left: 589px;
    top: 173px;
    width: 5px;
    height: 616px;
    background: var(--divider);
  }
  .producer-name {
    position: absolute;
    left: 40px;
    top: 833px;
    font-family: "Cabin", sans-serif;
    font-size: 26px;
    line-height: 32px;
    color: var(--ink);
  }
</style>
</head>
<body>
  <main class="postcard">
    <section class="invitation">
      <p class="lead-in">Join us for an evening of</p>
      <h1 class="event-title">Shadows<br>over Briarwick<br>Hall</h1>
      <p class="tagline">A night of dazzling attire,<br>fine food, and intrigue.</p>
      <p class="details">October 31, 2014<br>Dinner begins at 7<br>The Terrace at Briarwick</p>
      <p class="tickets">For Information and Tickets:<br>Go to <a href="#">www.LanternEventsKC.com</a><br>or call 816-555-0147</p>
    </section>
    <div class="divider"></div>
    <p class="producer-name">Lantern Events</p>
  </main>
</body>
</html>
```